For Sale Sign for Real Estate Agency

We need a For Sale Sign designed for our agency. I want a very simple/elegant sign that says "For Sale" towards the top of the sign (not in huge letters). Most of the sign should be a design/picture with our name and phone number somewhere at the bottom.

One significant detail, it's important that our logo not be too big or the center piece of the sign. Since our company name has the word "rent" in it, people assume the house is for rent, instead of for sale.

I attached our logo and a rough outline of the format I'm looking for.

Again, I'm looking for elegant and simple! Thanks for your time

Industry/Entity Type

Real Estate

Colors

Designer to choose colors to be used in the design.

Requirements
Must have
Nice to have
Should not have
• Nothing tacky!
• Our logo/company name should not be too big or the center piece of the sign. Since our company name has the word "rent" in it, people assume the house is for rent, instead of for sale.

```html
<!DOCTYPE html>
<html lang="en">
<head>
<meta charset="utf-8">
<title>For Sale Sign – Lindhurst Realty</title>
<link rel="stylesheet" href="https://fonts.googleapis.com/css2?family=Montserrat:wght@800&family=Barlow:wght@600&family=Nunito+Sans:wght@400&display=swap">
<style>
  :root {
    --sign-red: #ed1c24;
    --sign-red-soft: #f4585e;
    --sign-white: #ffffff;
    --ink: #231f20;
    --backdrop: #3e444d;
  }
  * { margin: 0; padding: 0; box-sizing: border-box; }
  html, body {
    width: 1200px;
    height: 837px;
    overflow: hidden;
    background: var(--backdrop);
  }
  .canvas {
    width: 1200px;
    height: 837px;
    display: flex;
    align-items: center;
    justify-content: center;
  }
  .sign {
    position: relative;
    width: 302px;
    height: 634px;
    background: var(--sign-white);
    overflow: hidden;
  }
  .sign__band {
    position: absolute;
    inset: 0;
    width: 302px;
    height: 634px;
  }
  .sign__illustration {
    position: absolute;
    top: 268px;
    left: 76px;
    width: 150px;
    height: 130px;
    border-radius: 12px;
    background: linear-gradient(180deg, var(--sign-red) 0%, var(--sign-red-soft) 100%);
  }
  .sign__title {
    position: absolute;
    top: 94px;
    left: 0;
    width: 100%;
    text-align: center;
    font-family: "Montserrat", sans-serif;
    font-weight: 800;
    font-size: 37px;
    letter-spacing: 0;
    line-height: 1;
    color: var(--sign-white);
  }
  .sign__agency {
    position: absolute;
    top: 500px;
    left: 0;
    width: 100%;
    text-align: center;
    font-family: "Nunito Sans", sans-serif;
    font-weight: 400;
    font-size: 20px;
    letter-spacing: 0.3px;
    color: var(--ink);
  }
  .sign__phone {
    position: absolute;
    top: 555px;
    left: 0;
    width: 100%;
    text-align: center;
    font-family: "Barlow", sans-serif;
    font-weight: 600;
    font-size: 31px;
    letter-spacing: 1.5px;
    line-height: 1;
    color: var(--ink);
  }
</style>
</head>
<body>
  <main class="canvas">
    <section class="sign" aria-label="For sale sign">
      <svg class="sign__band" viewBox="0 0 302 634" aria-hidden="true">
        <path fill="var(--sign-red)"
              d="M0 0 H302 V290 L162 214 Q151 208 140 214 L0 290 Z"/>
      </svg>
      <div class="sign__illustration" role="img" aria-label="Red house illustration with a four-pane window"></div>
      <h1 class="sign__title">FOR SALE</h1>
      <p class="sign__agency">Lindhurst Realty</p>
      <p class="sign__phone">555-204-318</p>
    </section>
  </main>
</body>
</html>
```